Business Card - Tally Forge

Need Business Card design for company named Tally Forge. Software development focused mainly on Brindle Kelvox & Vuro Apps. I've attached our logo with both a black and white background. Please add trademark symbol to logo when using.

```html
<!DOCTYPE html>
<html lang="en">
<head>
<meta charset="utf-8">
<title>Tally Forge – Business Card</title>
<link href="https://fonts.googleapis.com/css2?family=Arimo:wght@700&display=swap" rel="stylesheet">
<style>
  :root {
    --backdrop: #0b0f13;
    --front-top: #f43aa6;
    --front-bottom: #ff0f16;
    --back-top: #4a4a4a;
    --back-bottom: #060606;
    --accent: #ff6a00;
    --rule-dark: #2a1010;
    --brand-on-front: #1a1a1a;
    --brand-on-back: #ffffff;
    --band-end: #5a5a5a;
  }
  html, body {
    margin: 0;
    padding: 0;
    width: 1200px;
    height: 788px;
    overflow: hidden;
    background: var(--backdrop);
  }
  .canvas {
    position: relative;
    width: 1200px;
    height: 788px;
  }
  .card {
    position: absolute;
    top: 259px;
    width: 460px;
    height: 270px;
    overflow: hidden;
  }
  .card--front {
    left: 70px;
    background: linear-gradient(to bottom, var(--front-top), var(--front-bottom));
    border-bottom-left-radius: 28px;
  }
  .card--back {
    left: 670px;
    background: linear-gradient(to bottom, var(--back-top), var(--back-bottom) 70%);
    border-bottom-right-radius: 28px;
  }
  .edge-pill {
    position: absolute;
    width: 11px;
    height: 112px;
    border-radius: 6px;
    background: var(--accent);
  }
  .card--front .edge-pill--left { left: 20px; top: 130px; }
  .card--front .edge-pill--right { right: 20px; top: 22px; }
  .card--back .edge-pill--left { left: 20px; top: 40px; }
  .card--back .edge-pill--right { right: 20px; top: 150px; }
  .brand {
    position: absolute;
    left: 0;
    right: 0;
    text-align: center;
    font-family: "Arimo", Arial, sans-serif;
    font-weight: 700;
    font-size: 22px;
    display: flex;
    align-items: center;
    justify-content: center;
    gap: 10px;
  }
  .brand__mark {
    width: 14px;
    height: 14px;
    border-radius: 50%;
    background: var(--accent);
  }
  .card--front .brand { top: 70px; color: var(--brand-on-front); }
  .card--back .brand { top: 100px; color: var(--brand-on-back); }
  .contact-icon {
    position: absolute;
    width: 24px;
    height: 24px;
  }
  .contact-icon--pin { left: 120px; top: 178px; }
  .contact-icon--mail { left: 218px; top: 140px; }
  .contact-icon--phone { right: 78px; top: 100px; }
  .contact-rule {
    position: absolute;
    height: 2px;
    background: var(--rule-dark);
  }
  .contact-rule--one { left: 70px; width: 115px; top: 236px; }
  .contact-rule--two { left: 192px; width: 115px; top: 200px; }
  .contact-rule--three { left: 314px; width: 115px; top: 164px; }
  .back-band {
    position: absolute;
    left: 0;
    right: 0;
    top: 190px;
    height: 12px;
    background: linear-gradient(to right, var(--accent), var(--band-end) 75%, transparent);
  }
</style>
</head>
<body>
<main class="canvas">

  <section class="card card--front" aria-label="Card front">
    <span class="edge-pill edge-pill--left"></span>
    <span class="edge-pill edge-pill--right"></span>
    <div class="brand"><span class="brand__mark"></span>Tally Forge</div>

    <svg class="contact-icon contact-icon--phone" viewBox="0 0 24 24" aria-label="Phone">
      <path d="M5 3c1 0 3 3 3 4s-2 2-2 3 4 6 6 6 2-2 3-2 4 2 4 3-2 3-4 3C10 20 4 14 4 7c0-2 0-4 1-4z" fill="var(--accent)"/>
    </svg>
    <svg class="contact-icon contact-icon--mail" viewBox="0 0 24 24" aria-label="Email">
      <circle cx="12" cy="12" r="9" fill="none" stroke="var(--accent)" stroke-width="2"/>
      <circle cx="12" cy="12" r="3.5" fill="none" stroke="var(--accent)" stroke-width="2"/>
      <path d="M15.5 9v5c0 2 3 2 3-1" fill="none" stroke="var(--accent)" stroke-width="2"/>
    </svg>
    <svg class="contact-icon contact-icon--pin" viewBox="0 0 24 24" aria-label="Address">
      <path d="M8 4h8l-4 18z" fill="var(--accent)"/>
    </svg>

    <span class="contact-rule contact-rule--one"></span>
    <span class="contact-rule contact-rule--two"></span>
    <span class="contact-rule contact-rule--three"></span>
  </section>

  <section class="card card--back" aria-label="Card back">
    <span class="edge-pill edge-pill--left"></span>
    <span class="edge-pill edge-pill--right"></span>
    <div class="brand"><span class="brand__mark"></span>Tally Forge</div>
    <span class="back-band"></span>
  </section>

</main>
</body>
</html>
```